Brindle Search Business Card for recruitment company

We are looking for a Business Card Design that incorporates our personal details and our busines name and logo. We are a specialized search consultancy that recruit Property and Construction professionals.
We would like a business card that stands out and is appealing to the Construction and Property industry as well.

Target Market(s)

people in the construction and property industry

Contact Information for Business Card

Business Name and logo

Font styles to use
Serif

Colors
0094D4
00A9DD
6FCCEA
C7EBF8
E9F6FB

Requirements
Must have
• Business name and logo as well as contact details
Should not have
• No photos of us please

```html
<!DOCTYPE html>
<html lang="en">
<head>
<meta charset="utf-8">
<title>Brindle Search – Business Card</title>
<link href="https://fonts.googleapis.com/css2?family=Playfair+Display:wght@400;700&family=Lora:wght@400&display=swap" rel="stylesheet">
<style>
  :root {
    --backdrop: #b1b1ad;
    --blue-strong: #0094D4;
    --blue-mid: #00A9DD;
    --blue-light: #6FCCEA;
    --blue-pale: #C7EBF8;
    --blue-mist: #E9F6FB;
    --ink: #0076aa;
    --paper: #ffffff;
    --shadow: rgba(0, 0, 0, 0.22);
  }
  * { box-sizing: border-box; margin: 0; padding: 0; }
  html, body {
    width: 1200px;
    height: 801px;
    overflow: hidden;
    background: var(--backdrop);
  }
  .stage {
    position: relative;
    width: 1200px;
    height: 801px;
  }
  .card {
    position: absolute;
    top: 245px;
    width: 530px;
    height: 310px;
    border-radius: 28px;
    overflow: hidden;
    box-shadow: 0 14px 30px var(--shadow);
  }
  .card-front { left: 45px; background: var(--paper); }
  .card-back {
    left: 625px;
    background: linear-gradient(135deg, var(--blue-strong), var(--blue-mid));
    display: flex;
    align-items: center;
    justify-content: center;
  }

  .front-band {
    position: absolute;
    inset: 0;
    width: 100%;
    height: 100%;
  }
  .brand {
    display: flex;
    align-items: center;
    gap: 12px;
    white-space: nowrap;
  }
  .brand-dot {
    flex: none;
    border-radius: 50%;
  }
  .wordmark {
    font-family: "Playfair Display", serif;
    font-weight: 400;
    letter-spacing: 0.06em;
    text-transform: uppercase;
  }
  .front-brand {
    position: absolute;
    left: 34px;
    top: 40px;
    color: var(--ink);
  }
  .front-brand .brand-dot { width: 16px; height: 16px; background: var(--blue-strong); }
  .front-brand .wordmark { font-size: 22px; }
  .back-brand { color: var(--paper); }
  .back-brand .brand-dot { width: 26px; height: 26px; background: var(--blue-mist); }
  .back-brand .wordmark { font-size: 38px; }

  .accent-bar {
    position: absolute;
    left: 0;
    top: 118px;
    width: 14px;
    height: 44px;
    background: var(--blue-strong);
  }
  .identity {
    position: absolute;
    left: 34px;
    top: 118px;
    color: var(--ink);
  }
  .person-name {
    font-family: "Playfair Display", serif;
    font-weight: 700;
    font-size: 22px;
    letter-spacing: 0.03em;
    text-transform: uppercase;
  }
  .person-role {
    font-family: "Lora", serif;
    font-size: 12px;
    letter-spacing: 0.12em;
    text-transform: uppercase;
    color: var(--blue-strong);
    margin-top: 2px;
  }
  .contact-list {
    list-style: none;
    margin-top: 16px;
    font-family: "Lora", serif;
    font-size: 13px;
    line-height: 1.6;
  }
  .contact-list li { display: flex; align-items: center; gap: 8px; }
  .contact-icon { width: 11px; height: 11px; fill: none; stroke: var(--blue-strong); stroke-width: 1.6; flex: none; }
  .contact-icon.solid { fill: var(--blue-strong); stroke: none; }
</style>
</head>
<body>
<main class="stage">
  <section class="card card-front" aria-label="Business card front">
    <svg class="front-band" viewBox="0 0 530 310" preserveAspectRatio="none" aria-hidden="true">
      <defs>
        <linearGradient id="band-fill" x1="0" y1="0" x2="1" y2="1">
          <stop offset="0" stop-color="#0094D4"/>
          <stop offset="1" stop-color="#00A9DD"/>
        </linearGradient>
      </defs>
      <path d="M340 0 H530 V310 H462 C428 230 370 170 340 110 Z" fill="url(#band-fill)"/>
      <path d="M340 110 C370 170 428 230 462 310" fill="none" stroke="#6FCCEA" stroke-width="4"/>
    </svg>
    <div class="brand front-brand">
      <span class="brand-dot" aria-hidden="true"></span>
      <span class="wordmark">Brindle Search</span>
    </div>
    <span class="accent-bar"></span>
    <div class="identity">
      <p class="person-name">Jonah Pierce</p>
      <p class="person-role">Founder</p>
      <ul class="contact-list">
        <li>
          <svg class="contact-icon" viewBox="0 0 12 12"><path d="M2 1.5 L4 1.5 L5 4 L3.8 5 C4.5 6.5 5.5 7.5 7 8.2 L8 7 L10.5 8 L10.5 10 C6 10.5 1.5 6 2 1.5 Z"/></svg>
          +64 21 555 0147
        </li>
        <li>
          <svg class="contact-icon" viewBox="0 0 12 12"><rect x="1" y="2.5" width="10" height="7"/><path d="M1 2.5 L6 6.5 L11 2.5"/></svg>
          jonah@brindlesearch.nz
        </li>
        <li>
          <svg class="contact-icon" viewBox="0 0 12 12"><circle cx="6" cy="6" r="5"/><path d="M1 6 H11 M6 1 C3.5 3.5 3.5 8.5 6 11 C8.5 8.5 8.5 3.5 6 1"/></svg>
          www.brindlesearch.nz
        </li>
        <li>
          <svg class="contact-icon solid" viewBox="0 0 12 12"><path d="M6 0.5 C3.5 0.5 2 2.3 2 4.4 C2 7 6 11.5 6 11.5 C6 11.5 10 7 10 4.4 C10 2.3 8.5 0.5 6 0.5 Z M6 3 A1.4 1.4 0 1 1 6 5.8 A1.4 1.4 0 1 1 6 3 Z"/></svg>
          Auckland, New Zealand
        </li>
      </ul>
    </div>
  </section>

  <section class="card card-back" aria-label="Business card back">
    <div class="brand back-brand">
      <span class="brand-dot" aria-hidden="true"></span>
      <span class="wordmark">Brindle Search</span>
    </div>
  </section>
</main>
</body>
</html>
```